Create Bourbon label for Craft Distillery located in the Foothills of NC.

Need to create a label for a craft bourbon. The brand name is Creekhollow. Looking for a traditional/vintage bottle label. I have created a concept and would like an expansion of the concept idea (open to artwork outside of concept art as well). I have included the bottle being used. Label area approx 4.25H x 3.5W. With the Creekhollow brand name, would like to incorporate trees (native to NC and Appalachia), mountains (mt pano of area included), and sawblade. However, I do not want the sawblade to be the focal point of the design. The word Bourbon, proof, abv, and 750 ml will need to be horizontal. Creekhollow and Made in NC can be angled in the design.

Requirements
Must have
• Front Label will need to contain the followingBrand Name = SawmillsBourbon750 ml100 Proof50% ABVAged 3 years

```html
<!DOCTYPE html>
<html lang="en">
<head>
<meta charset="utf-8">
<title>Creekhollow Bourbon Label</title>
<link href="https://fonts.googleapis.com/css2?family=Rye&family=Oswald:wght@600&display=swap" rel="stylesheet">
<style>
  :root {
    --page: #ffffff;
    --forest-dark: #120f0b;
    --forest-mid: #2a2419;
    --forest-green: #1d2a1c;
    --gold-light: #f6dd7a;
    --gold: #d3a637;
    --gold-deep: #9b6d17;
    --ink-brown: #3a230c;
    --label-white: #ffffff;
    --banner-fill: #17130d;
  }
  html, body {
    margin: 0;
    padding: 0;
    width: 1200px;
    height: 1200px;
    overflow: hidden;
    background: var(--page);
  }
  .canvas {
    position: relative;
    width: 1200px;
    height: 1200px;
  }
  .bourbon-label {
    position: absolute;
    left: 190px;
    top: 105px;
    width: 820px;
    height: 988px;
    display: block;
  }
  .brand-name {
    font-family: "Rye", serif;
    fill: var(--label-white);
  }
  .product-type {
    font-family: "Rye", serif;
    fill: var(--ink-brown);
  }
  .spec-text {
    font-family: "Oswald", sans-serif;
    font-weight: 600;
    fill: var(--label-white);
    letter-spacing: 0.5px;
  }
  .origin-text {
    font-family: "Rye", serif;
    fill: var(--ink-brown);
  }
</style>
</head>
<body>
<main class="canvas">
  <svg class="bourbon-label" viewBox="0 0 440 530" xmlns="http://www.w3.org/2000/svg">
    <defs>
      <linearGradient id="forestTone" x1="0" y1="0" x2="1" y2="1">
        <stop offset="0" stop-color="var(--forest-mid)"/>
        <stop offset="0.5" stop-color="var(--forest-dark)"/>
        <stop offset="1" stop-color="var(--forest-green)"/>
      </linearGradient>
      <linearGradient id="goldFoil" x1="0" y1="0" x2="1" y2="1">
        <stop offset="0" stop-color="var(--gold-deep)"/>
        <stop offset="0.45" stop-color="var(--gold-light)"/>
        <stop offset="0.7" stop-color="var(--gold)"/>
        <stop offset="1" stop-color="var(--gold-deep)"/>
      </linearGradient>
    </defs>

    <!-- Background forest -->
    <rect class="forest-backdrop" width="440" height="530" fill="url(#forestTone)"
          role="img" aria-label="Dark photograph of tall forest tree trunks"/>

    <!-- Gold frame -->
    <g class="label-frame" fill="none" stroke="url(#goldFoil)">
      <path stroke-width="2.2" d="M24,14 H416 V24 H426 V506 H416 V516 H24 V506 H14 V24 H24 Z"/>
      <path stroke-width="1" d="M30,20 H410 V30 H420 V500 H410 V510 H30 V500 H20 V30 H30 Z"/>
    </g>

    <!-- Emblem artwork: evergreen treeline over a saw blade -->
    <ellipse class="emblem-art" cx="213" cy="235" rx="135" ry="185" fill="url(#goldFoil)"
             role="img" aria-label="Gold foil silhouette of evergreen trees rising above a circular saw blade"/>

    <!-- Angled name banner -->
    <g class="name-banner" transform="rotate(-9 215 303)">
      <rect x="25" y="263" width="380" height="80" fill="var(--banner-fill)" stroke="url(#goldFoil)" stroke-width="3"/>
      <rect x="31" y="269" width="368" height="68" fill="none" stroke="url(#goldFoil)" stroke-width="1"/>
      <text class="brand-name" x="215" y="320" text-anchor="middle" font-size="42"
            textLength="336" lengthAdjust="spacingAndGlyphs">CREEKHOLLOW</text>
    </g>

    <!-- Product type -->
    <text class="product-type" x="213" y="378" text-anchor="middle" font-size="25">BOURBON</text>
    <path class="product-underline" d="M150,392 Q213,412 276,392" fill="none" stroke="var(--ink-brown)" stroke-width="1.4"/>

    <!-- Specs -->
    <g class="spec-left">
      <text class="spec-text" x="97" y="476" text-anchor="middle" font-size="14">100</text>
      <text class="spec-text" x="97" y="494" text-anchor="middle" font-size="14">PROOF</text>
    </g>
    <g class="spec-right">
      <text class="spec-text" x="355" y="476" text-anchor="middle" font-size="14">50% ABV</text>
      <text class="spec-text" x="355" y="494" text-anchor="middle" font-size="14">750ML</text>
    </g>

    <!-- Origin ribbon -->
    <g class="origin-ribbon">
      <path d="M158,472 L268,472 L272,486 L268,500 L158,500 L154,486 Z" fill="url(#goldFoil)"/>
      <text class="origin-text" x="213" y="492" text-anchor="middle" font-size="15">MADE IN NC</text>
    </g>
  </svg>
</main>
</body>
</html>
```